Web Design Job: Condo Debts Collection Business needs a Web Design

I need a site for a client, who works with condo debts collection, and ensure all revenues provided by condo fees will be always available to the building manager of condo on a specific date, regardless of defaults.
I have the visual identity (logo, slogan and colors) of the company, and some requirements on layout (kind of slider, menu options, phone number on a noble position, etc) - maybe I can do a sketch, but I like the idea of give some freedom to designer.

*** PLEASE, we have no interest in templates. We want something new***
Updates

Reason: We need something new, different and exclusive. We do not want anything that looks like a "template". Thanks.

Target Market(s)

I have two targets for this design:
- Condominium's building manager. This target is looking for a solution to overdue debts on it's condo.
- Residents on condominiums. This target wants to live in a better place, where their neighbors pay their condominium fees on time.

Industry/Entity Type

Business

Number of Pages Required

1 page

Requirements
Must have
• - Slider with title, some short text related, a nice image (I prefer happy and/or peaceful family, people doing business, happy friends, and so on).
• - I have a special attention to menu. I'm looking for one I can have a nice effect, more elegant, charming, kind of innovative.
• - Phone number on the top (or clearly visible).
• - Member log in area or icon on the top (or clearly visible).
• - News/articles area.
• - Modern fonts, with good quality, sans-serif on areas where reading is more intensive (prefer Google web-fonts).
• - Colors specified on attached files.
Nice to have
• - Clear background color, cause it's better to read larger texts (like articles). Dark backgrounds makes reading difficult.
• - A site with effects (like shadows, lines, curves, gradients, lights) is usually pretty.
• - I pay attention on beautiful footers.
Should not have
• - Images with a lot of money (I don't sell richness, I sell tranquility, peace, harmony, safety).
• - Poor menu.

```html
<!DOCTYPE html>
<html lang="pt">
<head>
<meta charset="utf-8">
<title>Velora Cobrança</title>
<link href="https://fonts.googleapis.com/css2?family=Open+Sans:wght@400;600;700&family=Oswald:wght@400;500&display=swap" rel="stylesheet">
<style>
:root{
  --navy:#1f2b4d;
  --navy-deep:#18223d;
  --navy-bar:#141c33;
  --blue:#2f6fc4;
  --ink:#2a3350;
  --text:#5b6378;
  --muted:#9aa2b8;
  --line:#e1e4ec;
  --white:#ffffff;
}
*{box-sizing:border-box;margin:0;padding:0}
html,body{width:1200px;height:2460px;overflow:hidden}
body{font-family:"Open Sans",sans-serif;color:var(--text);background:var(--white);font-size:14px;line-height:1.55}
a{color:inherit;text-decoration:none}

.site-header{height:120px;background:var(--navy);position:relative;color:var(--white)}
.brand{position:absolute;left:60px;top:28px;display:flex;align-items:center;gap:12px;font-weight:700;font-size:30px;letter-spacing:2px}
.brand-mark{width:26px;height:26px;background:var(--white)}
.brand small{display:block;font-size:10px;letter-spacing:1px;font-weight:400;opacity:.8}
.top-contact{position:absolute;right:60px;top:18px;display:flex;gap:26px;align-items:center;font-size:13px}
.top-contact span{display:flex;align-items:center;gap:7px}
.login-btn{background:var(--blue);padding:6px 16px;border-radius:3px;font-weight:600;font-size:12px}
.main-nav{position:absolute;right:60px;top:72px;display:flex;gap:28px;font-size:13px;font-weight:700;letter-spacing:.5px}
.main-nav a.active{border-bottom:2px solid var(--blue);padding-bottom:6px}

.hero{height:520px;position:relative;background:linear-gradient(180deg,#b9c9a0 0%,#c9b690 45%,#7d8a6a 100%)}
.hero-copy{position:absolute;left:0;right:0;top:380px;text-align:center;color:var(--white);font-family:"Oswald",sans-serif;text-shadow:0 2px 6px rgba(0,0,0,.35)}
.hero-copy h1{font-size:58px;font-weight:500;letter-spacing:4px;line-height:1.1}
.hero-copy p{font-size:28px;letter-spacing:2px}
.hero-dots{position:absolute;top:612px;left:0;right:0;display:flex;justify-content:center;gap:8px}
.hero-dots i{width:10px;height:10px;border-radius:50%;background:rgba(255,255,255,.6)}
.hero-dots i.on{background:var(--white)}

.welcome{height:540px;padding:44px 60px;display:flex;gap:50px}
.welcome-main{width:700px}
h2.section-title{font-size:20px;font-weight:700;color:var(--ink);text-transform:uppercase;padding-bottom:10px;border-bottom:1px solid var(--line);margin-bottom:14px}
.welcome-main p{font-size:13px;margin-bottom:12px}
.welcome-main .lead{text-transform:uppercase;font-weight:600;color:var(--ink);font-size:12px}
.news{width:330px}
.news-item{padding:12px 0;border-bottom:1px solid var(--line)}
.news-item h3{font-size:14px;color:var(--ink);font-weight:700;line-height:1.4}
.news-item p{font-size:12px;color:var(--muted)}

.services{height:440px;background:var(--navy);padding-top:56px;color:var(--white)}
.services h2{text-align:center;font-size:24px;font-weight:700;letter-spacing:1px}
.services h2::after{content:"";display:block;width:50px;height:2px;background:var(--blue);margin:10px auto 0}
.service-cards{display:flex;gap:40px;justify-content:center;margin-top:30px}
.service-card{width:280px}
.service-photo{height:140px;border:4px solid var(--white)}
.service-card h3{font-size:15px;font-weight:700;margin:14px 0 8px;line-height:1.35}
.service-card p{font-size:12px;color:#b8c0d6}
.read-more{display:inline-block;margin-top:12px;font-size:12px;font-weight:700}

.proposal{height:480px;padding:40px 140px;display:flex;gap:40px}
.proposal-form{width:300px;background:var(--navy);color:var(--white)}
.proposal-form h2{background:var(--white);color:var(--ink);border:2px solid var(--navy);font-size:18px;font-weight:700;padding:14px 18px;text-transform:uppercase}
.proposal-form form{padding:18px}
.field{display:block;background:var(--white);color:var(--muted);font-size:12px;padding:8px 10px;margin-bottom:10px;height:34px}
.field.tall{height:80px}
.submit{display:inline-block;background:var(--blue);color:var(--white);font-weight:700;font-size:13px;padding:8px 28px;margin-top:4px}
.proposal-info{flex:1}
.proposal-info h2{font-size:24px;color:var(--ink);font-weight:700;line-height:1.3;text-transform:uppercase}
.proposal-info h3{font-size:15px;color:var(--blue);font-weight:700;text-transform:uppercase;margin:14px 0;padding-bottom:12px;border-bottom:1px solid var(--line)}
.proposal-info h4{font-size:14px;color:var(--ink);font-weight:700;text-transform:uppercase;margin-bottom:10px}
.benefits{list-style:none}
.benefits li{font-size:12px;padding:5px 0 5px 20px;position:relative}
.benefits li::before{content:"";position:absolute;left:2px;top:12px;width:7px;height:7px;border-radius:50%;background:var(--blue)}

.questions{height:80px;background:var(--navy-deep);color:var(--white);display:flex;align-items:center;padding:0 60px;gap:70px}
.questions strong{font-size:20px;line-height:1.1;font-weight:700}
.q-item{display:flex;align-items:center;gap:10px;font-size:11px;font-weight:600;line-height:1.3;text-transform:uppercase}
.q-item svg{flex:none}

.site-footer{height:240px;background:var(--navy);color:#c3c9dc;padding:30px 60px;display:flex;gap:50px;font-size:12px}
.site-footer h4{color:var(--white);font-size:13px;font-weight:700;text-transform:uppercase;margin-bottom:12px}
.f-col{width:240px}
.f-links{list-style:none}
.f-links li{line-height:1.7}
.newsletter-input{background:var(--white);color:var(--muted);padding:6px 8px;width:200px;margin-top:10px;font-size:11px}
.socials{display:flex;gap:10px}
.socials i{width:30px;height:30px;border-radius:50%;background:#c3c9dc;display:block}

.bottom-bar{height:40px;background:var(--navy-bar);color:#9aa2b8;font-size:11px;display:flex;align-items:center;justify-content:center;gap:18px}
</style>
</head>
<body>

<header class="site-header">
  <div class="brand"><span class="brand-mark"></span><div>VELORA<small>Cobrança Garantida</small></div></div>
  <div class="top-contact">
    <span><svg width="14" height="14" viewBox="0 0 24 24"><path fill="#fff" d="M6.6 10.8a15 15 0 006.6 6.6l2.2-2.2c.3-.3.7-.4 1-.2 1.1.4 2.3.6 3.6.6.6 0 1 .4 1 1V20c0 .6-.4 1-1 1A17 17 0 013 4c0-.6.4-1 1-1h3.5c.6 0 1 .4 1 1 0 1.3.2 2.5.6 3.6.1.3 0 .7-.2 1z"/></svg>(31) 4000-2718 &nbsp;|&nbsp; (31) 4000-5526</span>
    <span><svg width="14" height="12" viewBox="0 0 24 18"><rect x="1" y="1" width="22" height="16" fill="none" stroke="#fff" stroke-width="2"/><path d="M1 1l11 9 11-9" fill="none" stroke="#fff" stroke-width="2"/></svg>contato@veloracobranca.com.br</span>
    <a class="login-btn" href="#">ÁREA DO CLIENTE</a>
  </div>
  <nav class="main-nav">
    <a class="active" href="#">HOME</a><a href="#">ABOUT</a><a href="#">YOUR SLIP</a><a href="#">SERVICES</a><a href="#">NEWS</a><a href="#">PARTNERS</a><a href="#">CONTACT</a>
  </nav>
</header>

<section class="hero" role="img" aria-label="Photo of a smiling family outdoors in warm sunlight">
  <div class="hero-copy">
    <h1>LOREM IPSUM DOLOR SIT AMET</h1>
    <p>CONSECTETUR ADIPISCING ELIT</p>
  </div>
</section>
<div class="hero-dots" style="position:absolute"><i class="on"></i><i></i><i></i><i></i></div>

<section class="welcome">
  <div class="welcome-main">
    <h2 class="section-title">Welcome to Velora Cobrança</h2>
    <p class="lead">Cobrança garantida de condomínios</p>
    <p class="lead">Quer receber todas as taxas do seu condomínio em dia e ainda aumentar sua receita?</p>
    <p>A Velora Cobrança é uma empresa que faz a cobrança de condomínios de forma eficiente. Trabalhamos com o síndico para garantir que toda a receita esteja disponível na data certa, mesmo diante da inadimplência de alguns moradores do prédio.</p>
    <p>A Velora assume a gestão da cobrança e garante o repasse integral ao condomínio, trazendo mais tranquilidade, harmonia e segurança para todos.</p>
    <p>Oferecemos atendimento próximo, relatórios claros e acompanhamento mensal, para que o síndico possa focar no que realmente importa: o bem-estar dos moradores.</p>
  </div>
  <aside class="news">
    <h2 class="section-title">Latest News / Articles</h2>
    <div class="news-item"><h3>Lorem ipsum dolor sit amet, consectetur adipiscing elit</h3><p>Sed do eiusmod tempor incididunt ut labore et dolore magna aliqua.</p></div>
    <div class="news-item"><h3>Lorem ipsum dolor sit amet, consectetur adipiscing elit</h3><p>Sed do eiusmod tempor incididunt ut labore et dolore magna aliqua.</p></div>
    <div class="news-item"><h3>Lorem ipsum dolor sit amet, consectetur adipiscing elit</h3><p>Sed do eiusmod tempor incididunt ut labore et dolore magna aliqua.</p></div>
  </aside>
</section>

<section class="services">
  <h2>OUR SERVICES</h2>
  <div class="service-cards">
    <article class="service-card">
      <div class="service-photo" role="img" aria-label="Photo of people in a business meeting" style="background:linear-gradient(135deg,#8d9bb0,#5a6a85)"></div>
      <h3>Lorem ipsum dolor sit amet, consectetur adipiscing elit</h3>
      <p>Sed do eiusmod tempor incididunt ut labore et dolore magna aliqua.</p>
      <a class="read-more" href="#">Read more ›</a>
    </article>
    <article class="service-card">
      <div class="service-photo" role="img" aria-label="Photo of a team working together at a desk" style="background:linear-gradient(135deg,#b5a48a,#6e6656)"></div>
      <h3>Lorem ipsum dolor sit amet, consectetur adipiscing elit</h3>
      <p>Sed do eiusmod tempor incididunt ut labore et dolore magna aliqua.</p>
      <a class="read-more" href="#">Read more ›</a>
    </article>
    <article class="service-card">
      <div class="service-photo" role="img" aria-label="Photo of hands over documents on a table" style="background:linear-gradient(135deg,#9fb1c4,#4b5d7a)"></div>
      <h3>Lorem ipsum dolor sit amet, consectetur adipiscing elit</h3>
      <p>Sed do eiusmod tempor incididunt ut labore et dolore magna aliqua.</p>
      <a class="read-more" href="#">Read more ›</a>
    </article>
  </div>
</section>

<section class="proposal">
  <div class="proposal-form">
    <h2>Ask for your proposal</h2>
    <form>
      <span class="field">Name</span>
      <span class="field">E-mail</span>
      <span class="field">Phone</span>
      <span class="field tall">Message</span>
      <span class="submit">SUBMIT</span>
    </form>
  </div>
  <div class="proposal-info">
    <h2>Conheça a Velora Cobrança e solucione seus problemas</h2>
    <h3>Conheça a Velora Cobrança e solucione seus problemas</h3>
    <h4>Vantagens de ser um cliente Velora</h4>
    <ul class="benefits">
      <li>Antecipação de 100% da receita do condomínio, eliminando toda inadimplência</li>
      <li>Otimização dos condomínios adimplentes</li>
      <li>Controle interno das finanças, contas de cobrança e despesas judiciais</li>
      <li>Antecipação de receita para reformas e melhorias do condomínio</li>
      <li>Antecipação da receita do condomínio com prazo reduzido e sem burocracia</li>
      <li>Eliminação de problemas decorrentes da cobrança feita pelo síndico</li>
    </ul>
  </div>
</section>

<section class="questions">
  <strong>HAVE<br>QUESTIONS?</strong>
  <div class="q-item"><svg width="26" height="26" viewBox="0 0 24 24"><path fill="#fff" d="M6.6 10.8a15 15 0 006.6 6.6l2.2-2.2c.3-.3.7-.4 1-.2 1.1.4 2.3.6 3.6.6.6 0 1 .4 1 1V20c0 .6-.4 1-1 1A17 17 0 013 4c0-.6.4-1 1-1h3.5c.6 0 1 .4 1 1 0 1.3.2 2.5.6 3.6.1.3 0 .7-.2 1z"/></svg><span>Call us<br>(31) 4000-2718</span></div>
  <div class="q-item"><svg width="26" height="20" viewBox="0 0 24 18"><rect x="1" y="1" width="22" height="16" fill="none" stroke="#fff" stroke-width="2"/><path d="M1 1l11 9 11-9" fill="none" stroke="#fff" stroke-width="2"/></svg><span>Send us<br>an email</span></div>
  <div class="q-item"><svg width="22" height="28" viewBox="0 0 20 28"><path fill="#fff" d="M10 0a10 10 0 00-10 10c0 7 10 18 10 18s10-11 10-18A10 10 0 0010 0zm0 14a4 4 0 110-8 4 4 0 010 8z"/></svg><span>Find a<br>local office</span></div>
  <div class="q-item"><svg width="26" height="26" viewBox="0 0 24 24"><circle cx="12" cy="12" r="10" fill="none" stroke="#fff" stroke-width="2"/><path d="M9 9a3 3 0 115 2.2c-1 .7-2 1.3-2 2.8M12 17.5v.5" fill="none" stroke="#fff" stroke-width="2"/></svg><span>Read the<br>FAQs</span></div>
</section>

<footer class="site-footer">
  <div class="f-col">
    <h4>Contact us</h4>
    <p>Rua das Acácias, 120<br>Jardim Norte<br>Cidade Alta</p>
    <p style="margin-top:10px">(31) 4000-2718</p>
  </div>
  <div class="f-col">
    <h4>Subscribe our newsletter</h4>
    <p>Lorem ipsum dolor sit amet, consectetur adipiscing elit.</p>
    <div class="newsletter-input">Your e-mail</div>
  </div>
  <div class="f-col">
    <h4>Quick links</h4>
    <ul class="f-links"><li>Home</li><li>About</li><li>Your Slip</li><li>Services</li><li>News</li><li>Partners</li><li>Contact</li></ul>
  </div>
  <div class="f-col">
    <h4>Connect with Velora</h4>
    <div class="socials"><i></i><i></i><i></i></div>
  </div>
</footer>

<div class="bottom-bar">
  <span>© 2015 Velora. All Rights Reserved</span><span>•</span><span>Terms and Conditions</span><span>•</span><span>Privacy Policy</span><span>•</span><span>Terms of Use</span>
</div>

</body>
</html>
```